Design Card that Captures Life's Moments

Thinking black and white design with maybe some accent colors. Open to others too. Looking for bold and modern to accompany new logo design. For the side without my info, would have tagline of "Capturing Life's Moments" with either logo or website petravossimaging.com. I want the tagline to dominate and be the main focus of that side.

Target Market(s)

Something that can appeal to people who might be interested in family/kids, business, sports, commercial, or birth/newborn photography.

Industry/Entity Type

Professional Photography

Contact Information for Business Card

Font styles to use
Sans Serif
Script
Other font styles liked:
• Go with Logo, but the tagline could be script that popped.

Requirements
Must have
• See details above! Wow factor! Make someone pick my card up and take it home or at least to look at it further.
• Tagline: Capturing Life's Moments (Main text on side without name)
• INFO:
• Petra Voss-Hale - Photographer
• 555-318-0462 - Cell and for SMS
• www.petravossimaging.com - Website (maybe on side with tagline?)
• petra@petrastudioframes.com - Email
Nice to have
• JUST AN IDEA... I would like to see Capturing Life's Moment really take over most of one side of the card. Think greeting card. Where you can't miss it. It is in your face, but nice and elegant. Maybe cursive, but could work with other font. Instead of logo on tagline side, just have petravossimaging.com in smaller text along one of the edges.
Should not have
• Too simple I could of created it, like with only my logo and some typed text.

```html
<!DOCTYPE html>
<html lang="en">
<head>
<meta charset="utf-8">
<title>Petra Voss Imaging – Business Card</title>
<link rel="stylesheet" href="https://fonts.googleapis.com/css2?family=Dancing+Script:wght@700&family=Oswald:wght@400;700&family=Open+Sans:wght@300;400&display=swap">
<style>
  :root {
    --page-bg: #e4e4e2;
    --card-white: #ffffff;
    --ink-black: #0b0b0b;
    --ink-grey: #444444;
    --rule-white: #f2f2f2;
  }
  * { box-sizing: border-box; margin: 0; padding: 0; }
  html, body {
    width: 1200px;
    height: 982px;
    overflow: hidden;
    background: var(--page-bg);
  }
  .canvas {
    position: relative;
    width: 1200px;
    height: 982px;
    display: flex;
    align-items: center;
    justify-content: center;
    gap: 60px;
  }
  .card {
    position: relative;
    width: 520px;
    height: 297px;
    background: var(--card-white);
    box-shadow: 0 6px 18px rgba(0,0,0,0.18);
    overflow: hidden;
  }

  /* Front: contact side */
  .brand-mark {
    position: absolute;
    left: 150px;
    top: 34px;
    width: 220px;
    text-align: center;
    border-top: 1.5px solid var(--ink-black);
    border-bottom: 1.5px solid var(--ink-black);
    padding: 7px 0 6px;
    font-family: "Open Sans", sans-serif;
    font-weight: 300;
    font-size: 17px;
    letter-spacing: 2px;
    color: var(--ink-grey);
  }
  .person-name {
    position: absolute;
    left: 0;
    width: 100%;
    top: 88px;
    text-align: center;
    font-family: "Oswald", sans-serif;
    font-weight: 700;
    font-size: 36px;
    letter-spacing: 1px;
    color: var(--ink-black);
    text-transform: uppercase;
  }
  .person-role {
    position: absolute;
    left: 0;
    width: 100%;
    top: 144px;
    text-align: center;
    font-family: "Oswald", sans-serif;
    font-weight: 400;
    font-size: 15px;
    letter-spacing: 9px;
    color: var(--ink-black);
    text-transform: uppercase;
  }
  .contact-band {
    position: absolute;
    left: 0;
    right: 0;
    top: 196px;
    height: 66px;
    background: var(--ink-black);
    border-top: 3px solid var(--card-white);
    outline: 2px solid var(--ink-black);
    display: flex;
    flex-direction: column;
    justify-content: center;
    align-items: center;
    gap: 4px;
    font-family: "Open Sans", sans-serif;
    font-weight: 400;
    font-size: 13.5px;
    color: var(--card-white);
  }
  .contact-line .divider { margin: 0 9px; }

  /* Back: tagline side */
  .card--tagline .panel {
    position: absolute;
    inset: 12px;
    background: var(--ink-black);
    display: flex;
    flex-direction: column;
    align-items: center;
    justify-content: center;
  }
  .card--tagline .panel-frame {
    position: absolute;
    inset: 6px;
    border: 1px solid var(--rule-white);
    pointer-events: none;
  }
  .tagline-brand {
    font-family: "Open Sans", sans-serif;
    font-weight: 300;
    font-size: 13px;
    letter-spacing: 2px;
    color: var(--rule-white);
    margin-bottom: 2px;
  }
  .tagline {
    width: 440px;
    text-align: center;
    white-space: nowrap;
    font-family: "Dancing Script", cursive;
    font-weight: 700;
    font-size: 44px;
    line-height: 1.15;
    color: var(--rule-white);
    border-bottom: 1.5px solid var(--rule-white);
    padding-bottom: 2px;
  }
  .tagline-web {
    margin-top: 8px;
    font-family: "Open Sans", sans-serif;
    font-weight: 400;
    font-size: 13px;
    letter-spacing: 0.5px;
    color: var(--rule-white);
  }
</style>
</head>
<body>
<main class="canvas">
  <section class="card card--contact" aria-label="Card front with contact details">
    <div class="brand-mark">Petra Voss Imaging</div>
    <h1 class="person-name">Petra Voss-Hale</h1>
    <p class="person-role">Photographer</p>
    <div class="contact-band">
      <p class="contact-line">petravossimaging.com<span class="divider">|</span>555-318-0462</p>
      <p class="contact-line">petra@petrastudioframes.com<span class="divider">|</span>Alder Falls, VA</p>
    </div>
  </section>

  <section class="card card--tagline" aria-label="Card back with tagline">
    <div class="panel">
      <div class="panel-frame"></div>
      <p class="tagline-brand">Petra Voss Imaging</p>
      <h2 class="tagline">Capturing Life's Moments</h2>
      <p class="tagline-web">www.petravossimaging.com</p>
    </div>
  </section>
</main>
</body>
</html>
```